Brightmoor Surface Index

I have a current web site that it looking quite aged and it needs a new lease of life. This is a Graffiti Management Website so is all about data processing and management of information. I want a html 5 view on any platform design. clean crisp and new. I have provided some screen shots of my current site.

Target Market(s)

The Target Market will be local government. most users will not be heavy pc users

Industry/Entity Type

Management

Font styles to use
Sans Serif
Other font styles liked:
• web font like calibri

Colors

Designer to choose colors to be used in the design.

Requirements
Must have
• Must have menus similar to attachments

```html
<!DOCTYPE html>
<html lang="en">
<head>
<meta charset="utf-8">
<title>Brightmoor Surface Index</title>
<link rel="stylesheet" href="https://fonts.googleapis.com/css2?family=Open+Sans:wght@300;400;600;700;800&display=swap">
<style>
:root{
  --navy:#12136e;
  --sky:#2b9ad6;
  --band:#5aafdf;
  --band-dark:#4fa5d6;
  --head:#55a2d8;
  --ink:#333;
  --muted:#777;
  --white:#fff;
  --gray:#efefef;
}
*{margin:0;padding:0;box-sizing:border-box}
html,body{width:763px;height:1200px;overflow:hidden}
body{position:relative;font-family:"Open Sans",Arial,sans-serif;color:var(--ink);background:var(--white)}
.abs{position:absolute}

.masthead{left:0;top:0;width:763px;height:50px;background:var(--head)}
.brand-name{left:0;top:5px;width:763px;text-align:center;color:var(--white);font-weight:700;font-size:22px;letter-spacing:22px;padding-left:22px;line-height:30px}
.brand-bar{left:0;top:38px;width:763px;height:12px;background:var(--navy)}
.brand-tag{left:0;top:39px;width:763px;text-align:center;color:var(--white);font-size:7.5px;font-weight:700;letter-spacing:1.6px;line-height:10px}

.nav{left:0;top:50px;width:763px;height:58px;background:var(--white)}
.nav a{position:absolute;top:26px;transform:translateX(-50%);font-size:8px;font-weight:600;color:#222;text-decoration:none;white-space:nowrap}
.nav a.active{color:var(--sky)}

.hero{left:0;top:108px;width:763px;height:394px;
  background:linear-gradient(100deg,#d9dcd8 0%,#eef0ec 30%,#c7ccca 55%,#e3e5e3 80%,#cfd1cf 100%)}
.hero-title{left:88px;top:237px;color:var(--white);font-size:23px;font-weight:800;line-height:26px}
.hero-sub{left:88px;top:302px;color:var(--white);font-size:13.5px;line-height:19px}
.btn{position:absolute;display:flex;align-items:center;justify-content:center;color:var(--white);font-size:8px;font-weight:600;text-decoration:none}
.btn-dark{background:var(--navy)}
.btn-light{background:var(--sky)}
.arrow{width:30px;height:30px;border-radius:50%;border:2px solid #777;background:rgba(255,255,255,.5)}

.features{left:0;top:502px;width:763px;height:362px;background:linear-gradient(#f6f6f6,#fff 40%)}
.feature{position:absolute;width:180px;transform:translateX(-50%);text-align:center}
.feature svg{display:block;margin:0 auto;width:36px;height:36px}
.feature h3{margin-top:8px;font-size:11px;font-weight:600;color:var(--navy);letter-spacing:.2px;white-space:nowrap}
.feature p{margin-top:12px;font-size:7.5px;line-height:11.7px;color:var(--muted)}

.cta{left:0;top:864px;width:763px;height:104px;background:var(--gray)}
.cta-box{left:88px;top:886px;width:587px;height:60px;background:var(--white)}
.cta-text{left:108px;top:901px;font-size:20px;font-weight:300;color:var(--navy);line-height:28px}

.footer{left:0;top:968px;width:763px;height:184px;background:var(--band)}
.footer h4{position:absolute;top:22px;color:var(--white);font-size:9.5px;font-weight:600}
.divider{position:absolute;top:36px;width:1px;height:120px;background:#4b9dcc}
.links{position:absolute;left:88px;top:50px;list-style:none}
.links li{font-size:8px;color:var(--white);line-height:15.2px}
.field{position:absolute;left:260px;width:142px;height:26px;background:var(--white);font-size:7px;color:#888;padding:9px 6px}
.news{position:absolute;left:491px;width:185px;height:44px}
.news .day{position:absolute;left:0;top:0;width:20px;text-align:center;color:var(--white);font-size:15px;font-weight:700;line-height:16px}
.news .mon{position:absolute;left:0;top:16px;width:20px;text-align:center;color:var(--white);font-size:8.5px;line-height:10px}
.news .rule{position:absolute;left:27px;top:0;width:1px;height:36px;background:#4b9dcc}
.news p{position:absolute;left:35px;top:-1px;width:160px;font-size:7.5px;line-height:12px;color:var(--white);font-weight:600;white-space:nowrap}
.news-sep{left:519px;top:1071px;width:158px;height:1px;background:#7cc0e6}

.base{left:0;top:1152px;width:763px;height:48px;background:var(--band);border-top:1px solid var(--band-dark)}
.copyright{left:88px;top:1172px;font-size:7.5px;color:var(--white)}
.social{position:absolute;top:1168px;width:19px;height:19px;border-radius:50%;border:2px solid var(--white)}
</style>
</head>
<body>

<header>
  <div class="abs masthead"></div>
  <div class="abs brand-name">BSI</div>
  <div class="abs brand-bar"></div>
  <div class="abs brand-tag">BRIGHTMOOR SURFACE INDEX</div>
  <nav class="abs nav">
    <a class="active" style="left:115px">HOME</a>
    <a style="left:190px">PRODUCTS</a>
    <a style="left:289px">REPORTS BENIFITS</a>
    <a style="left:391px">LEGISLATION</a>
    <a style="left:483px">CONTACT US</a>
    <a style="left:558px">LOGIN</a>
    <a style="left:634px">DEMO LOGIN</a>
  </nav>
</header>

<section>
  <div class="abs hero" role="img" aria-label="Photo of a smiling woman at a laptop holding a coffee cup in a bright kitchen"></div>
  <h1 class="abs hero-title">BSI IS AN ONLINE<br>DATABASE SYSTEM</h1>
  <p class="abs hero-sub">TO MANAGE GRAFFITI IN YOUR AREA<br>OR YOUR PROPERTIES</p>
  <a class="btn btn-dark" style="left:88px;top:355px;width:78px;height:30px">LEARN MORE</a>
  <a class="btn btn-light" style="left:176px;top:355px;width:78px;height:30px">GET STARTED</a>
  <div class="abs arrow" style="left:19px;top:289px">
    <svg width="26" height="26" viewBox="0 0 26 26"><path d="M16 6 L8 13 L16 20 Z" fill="#777"/></svg>
  </div>
  <div class="abs arrow" style="left:706px;top:289px">
    <svg width="26" height="26" viewBox="0 0 26 26"><path d="M10 6 L18 13 L10 20 Z" fill="#777"/></svg>
  </div>
</section>

<section class="abs features">
  <div class="feature" style="left:174px;top:48px">
    <svg viewBox="0 0 36 36" fill="none" stroke="#12136e" stroke-width="3"><path d="M24 8H6v22h22V14"/><path d="M14 22l2-6 14-14 4 4-14 14z" fill="#12136e"/></svg>
    <h3>GRAFFITI REGISTER</h3>
    <p>BSI provides a National Register of Vandal-<br>ism and Graffiti. Subscribers to the BSI Da-<br>tabase can Add, Change, Report on and Archive<br>their own Graffiti Jobs</p>
  </div>
  <div class="feature" style="left:381px;top:48px">
    <svg viewBox="0 0 36 36" fill="none" stroke="#12136e" stroke-width="2.5"><rect x="3" y="12" width="22" height="18"/><path d="M10 12l18-8 6 18-9 5"/><path d="M5 28l6-8 5 5 3-3 5 6z" fill="#12136e"/><circle cx="18" cy="17" r="2" fill="#12136e"/></svg>
    <h3>GRAFFITI PHOTOS</h3>
    <p>BSI provides a National Register of Vandal-<br>ism and Graffiti. Subscribers to the BSI Da-<br>tabase can Add, Change, Report on and Archive<br>their own Graffiti Jobs</p>
  </div>
  <div class="feature" style="left:594px;top:48px">
    <svg viewBox="0 0 36 36" fill="#12136e"><rect x="15" y="2" width="14" height="12" transform="rotate(35 22 8)"/><rect x="12" y="14" width="8" height="10" transform="rotate(35 16 19)"/><path d="M5 24l7 5-5 6-5-3z"/><circle cx="30" cy="27" r="2"/></svg>
    <h3>GRAFFITI ARCHIVE</h3>
    <p>BSI provides a National Register of Vandal-<br>ism and Graffiti. Subscribers to the BSI Da-<br>tabase can Add, Change, Report on and Archive<br>their own Graffiti Jobs</p>
  </div>
  <div class="feature" style="left:174px;top:190px">
    <svg viewBox="0 0 36 36" fill="#12136e"><ellipse cx="14" cy="6" rx="11" ry="4"/><rect x="3" y="8" width="22" height="7" rx="3"/><rect x="3" y="16" width="22" height="7" rx="3"/><ellipse cx="24" cy="21" rx="10" ry="4"/><rect x="14" y="24" width="20" height="5" rx="3"/><rect x="14" y="30" width="20" height="5" rx="3"/></svg>
    <h3>SEARCHABLE DATABASE</h3>
    <p>BSI provides a National Register of Vandal-<br>ism and Graffiti. Subscribers to the BSI Da-<br>tabase can Add, Change, Report on and Archive<br>their own Graffiti Jobs</p>
  </div>
  <div class="feature" style="left:381px;top:190px">
    <svg viewBox="0 0 36 36" fill="#12136e"><rect x="3" y="20" width="5" height="13"/><rect x="10" y="16" width="5" height="17"/><rect x="17" y="19" width="5" height="14"/><rect x="24" y="12" width="5" height="21"/><path d="M3 16l9-7 7 5 9-9" fill="none" stroke="#12136e" stroke-width="2.5"/><path d="M26 3h6v6z"/></svg>
    <h3>STATISITCAL ANALYSIS REPORTS</h3>
    <p>BSI provides a National Register of Vandal-<br>ism and Graffiti. Subscribers to the BSI Da-<br>tabase can Add, Change, Report on and Archive<br>their own Graffiti Jobs</p>
  </div>
  <div class="feature" style="left:594px;top:190px">
    <svg viewBox="0 0 36 36" fill="none" stroke="#12136e" stroke-width="2.5"><rect x="12" y="3" width="18" height="24"/><rect x="5" y="10" width="18" height="24" fill="#fff"/><path d="M9 16h10M9 21h10M9 26h10M9 30h6"/></svg>
    <h3>DATA CONVERSION</h3>
    <p>BSI provides a National Register of Vandal-<br>ism and Graffiti. Subscribers to the BSI Da-<br>tabase can Add, Change, Report on and Archive<br>their own Graffiti Jobs</p>
  </div>
</section>

<section>
  <div class="abs cta"></div>
  <div class="abs cta-box"></div>
  <h2 class="abs cta-text">Helping You Clean up Your Community</h2>
  <a class="btn btn-light" style="left:578px;top:901px;width:79px;height:30px;box-shadow:0 1px 2px rgba(0,0,0,.2)">GET STARTED</a>
</section>

<footer>
  <div class="abs footer">
    <h4 style="left:88px">QUICK LINKS</h4>
    <h4 style="left:260px">NEWSLETTER</h4>
    <h4 style="left:491px">OUR NEWS</h4>
    <div class="divider" style="left:200px"></div>
    <div class="divider" style="left:449px"></div>
    <ul class="links">
      <li>Home</li><li>Products</li><li>Reports Benifits</li><li>Legislation</li><li>contact us</li><li>Login</li><li>Demo login</li>
    </ul>
  </div>
  <div class="field" style="top:1022px">Name:</div>
  <div class="field" style="top:1058px">Email:</div>
  <a class="btn btn-dark" style="left:260px;top:1094px;width:67px;height:26px">SUBMIT</a>

  <div class="news" style="top:1025px">
    <div class="day">23</div><div class="mon">nov</div><div class="rule"></div>
    <p>Sed ut perspiciatis unde omnis iste<br>natus error sit voluptatem accusantium<br>doloremque laudantium.</p>
  </div>
  <div class="abs news-sep"></div>
  <div class="news" style="top:1093px">
    <div class="day">23</div><div class="mon">nov</div><div class="rule"></div>
    <p>Sed ut perspiciatis unde omnis iste<br>natus error sit voluptatem accusantium<br>doloremque laudantium.</p>
  </div>

  <div class="abs base"></div>
  <p class="abs copyright">Copyright 2014 BSI all rights reserved</p>
  <span class="social" style="left:540px;background:#c4302b"></span>
  <span class="social" style="left:562px;background:#1d8fd0"></span>
  <span class="social" style="left:585px;background:#2c4a8c"></span>
  <span class="social" style="left:608px;background:#d64632"></span>
  <span class="social" style="left:631px;background:#e8641b"></span>
  <span class="social" style="left:654px;background:#1a7ab5"></span>
</footer>

</body>
</html>
```